New business card design to go with our new logo

just want an eye-catching business card to go with our new logo. We are open to double sided or single sided. Just want it to have the following info on it. Whatever layout you think looks best.

First and Last Name
Title
Phone 801-555-0187
Address 312 W. Larkmoor Avenue Orem UT 84057
Email thecrew@meadowstailandkennel.example

Industry/Entity Type

Business

```html
<!DOCTYPE html>
<html lang="en">
<head>
<meta charset="utf-8">
<title>Meadows Tail &amp; Kennel — Business Card</title>
<link rel="stylesheet" href="https://fonts.googleapis.com/css2?family=Open+Sans:wght@600;700&display=swap">
<style>
  :root {
    --backdrop: #bfe6dc;
    --card: #231f20;
    --ink: #ffffff;
    --accent-orange: #f0892f;
    --accent-blue: #1ba3dd;
  }
  * { box-sizing: border-box; margin: 0; padding: 0; }
  html, body { width: 1200px; height: 856px; overflow: hidden; }
  body {
    background: var(--backdrop);
    font-family: "Open Sans", Arial, sans-serif;
    display: flex;
    align-items: center;
    justify-content: center;
    gap: 40px;
  }
  .card {
    position: relative;
    width: 540px;
    height: 309px;
    background: var(--card);
    border-radius: 30px;
    color: var(--ink);
    box-shadow: 0 10px 24px rgba(0,0,0,0.18);
    overflow: hidden;
  }
  .brand {
    display: flex;
    align-items: center;
    gap: 12px;
    white-space: nowrap;
  }
  .brand-dot {
    width: 34px; height: 34px;
    border-radius: 50%;
    background: var(--accent-blue);
    flex: none;
  }
  .brand-name {
    font-weight: 700;
    color: var(--accent-orange);
    font-size: 26px;
    line-height: 1.1;
    letter-spacing: 0.5px;
  }
  .card-back .brand {
    position: absolute;
    left: 50%; top: 50%;
    transform: translate(-50%, -50%);
  }
  .card-front .brand {
    position: absolute;
    left: 36px; top: 112px;
  }
  .card-front .brand-name { font-size: 22px; }
  .identity {
    position: absolute;
    right: 34px; top: 26px;
    text-align: right;
    font-weight: 700;
    font-size: 13px;
    line-height: 1.4;
  }
  .contact {
    position: absolute;
    right: 30px; bottom: 44px;
    list-style: none;
    font-weight: 700;
    font-size: 12.5px;
    white-space: nowrap;
  }
  .contact li {
    display: flex;
    align-items: center;
    gap: 10px;
    margin-top: 6px;
  }
  .contact-icon {
    width: 16px; height: 16px;
    flex: none;
  }
</style>
</head>
<body>
  <section class="card card-front">
    <div class="identity">
      <p class="person-name">First and Last Name</p>
      <p class="person-title">Title</p>
    </div>
    <div class="brand">
      <span class="brand-dot"></span>
      <span class="brand-name">Meadows Tail &amp; Kennel</span>
    </div>
    <ul class="contact">
      <li>
        <svg class="contact-icon" viewBox="0 0 16 16" aria-hidden="true">
          <circle cx="8" cy="8" r="8" fill="var(--accent-orange)"/>
          <path d="M5.2 4.2l1.5 1.5-.8 1.1c.5 1.2 1.4 2.1 2.6 2.6l1.1-.8 1.5 1.5-1 1.2C7.6 11 5 8.4 4.2 5.2z" fill="#fff"/>
        </svg>
        <span>Phone 801-555-0187</span>
      </li>
      <li>
        <svg class="contact-icon" viewBox="0 0 16 16" aria-hidden="true">
          <circle cx="8" cy="8" r="8" fill="var(--accent-orange)"/>
          <path d="M8 3.5a3 3 0 0 0-3 3c0 2.2 3 6 3 6s3-3.8 3-6a3 3 0 0 0-3-3z" fill="#fff"/>
          <circle cx="8" cy="6.5" r="1.1" fill="var(--accent-orange)"/>
        </svg>
        <span>312 W. Larkmoor Avenue Orem UT 84057</span>
      </li>
      <li>
        <svg class="contact-icon" viewBox="0 0 16 16" aria-hidden="true">
          <circle cx="8" cy="8" r="8" fill="var(--accent-orange)"/>
          <rect x="4" y="5.2" width="8" height="5.6" rx="0.6" fill="#fff"/>
          <path d="M4.3 5.6L8 8.5l3.7-2.9" fill="none" stroke="var(--accent-orange)" stroke-width="0.9"/>
        </svg>
        <span>thecrew@meadowstailandkennel.example</span>
      </li>
    </ul>
  </section>

  <section class="card card-back">
    <div class="brand">
      <span class="brand-dot"></span>
      <span class="brand-name">Meadows Tail &amp; Kennel</span>
    </div>
  </section>
</body>
</html>
```